2 page brouchure for a Property Valuation company.

We require a 2 page brochure (printed front and back) for a property valuation company known as 'Brookmere Valuations'.

Brookmere valuations provides independent, reliable, accurate valuation services to our clients on the value of their properties to enable confidence and certainty in their decision.

The brochure is to be used to convey that the company provides valuation services for 8 main purposes and across 4 different property types.

The 8 main purposes for valuation include:
- Pre-Purchase Valuations
- Stamp Duty Valuations
-Capital Gains Tax (CGT)Valuations
-Unit Entitlement Valuations
-Family Law and Litigation Valuations
-Easement Valuations
-Wills & Probate Valuations
-Insolvency/Asset Realisation Valuations

The 4 main property types are:
-Residential
-Commercial
-Industrial
-Retail.

The brochure should have a title page, a page for the services, a page for the property types and a rear page with contact details.
Contact detail will include;
email:
phone :
Post :
website:

The words 'property valuation and advisory services' should be used at the front of the brochure.

The brochure should be professional and is used to convey information using visual aid and is to be used for promotion.

Our main colors are dark green and grey as seen in our logo.

We have attached our logo to add to the brochure and visit our website at: www.brookmerevaluations-example.com.au for more information about the company.

Please let me know if there are any further questions.

Target Market(s)

Solicitors/Lawyers
Accountants
Surveyors
Builders/Developers

Requirements
Must have
• Logo Colors, Logo, 8 Main services, 4 main property types, contact details.
Nice to have
• Should have concise visual aids to convey message.

Please add that we provide fast 48 hour turnaround for short form valuations. Maybe use a visual aid to convey this.

```html
<!DOCTYPE html>
<html lang="en">
<head>
<meta charset="utf-8">
<title>Brookmere Valuations – Brochure</title>
<link rel="stylesheet" href="https://fonts.googleapis.com/css2?family=Roboto:wght@400;500;700&family=Roboto+Condensed:wght@700&display=swap">
<style>
  :root{
    --green:#0d6b35;
    --green-dark:#0a5a2c;
    --ink:#2b2b2b;
    --icon:#3a3a3a;
    --grey-box:#2f2f30;
    --paper:#ffffff;
    --rule:#9aa0a6;
  }
  *{margin:0;padding:0;box-sizing:border-box}
  html,body{width:1200px;height:1181px;overflow:hidden;background:var(--paper)}
  body{position:relative;font-family:"Roboto",Arial,sans-serif;color:var(--ink)}
  .page{position:absolute;overflow:hidden}

  /* Cover */
  .cover{left:430px;top:44px;width:328px;height:479px}
  .cover-photo{position:absolute;inset:0;
    background:linear-gradient(180deg,#b9cfe6 0%,#d7e3ef 35%,#c9d6e2 55%,#8f9aa3 78%,#6c7468 100%)}
  .brand{position:absolute;left:123px;top:24px;display:flex;align-items:center;gap:10px}
  .brand-mark{width:41px;height:41px;background:var(--green)}
  .brand-name{font-weight:500;font-size:15px;letter-spacing:1.5px;line-height:17px;color:var(--green-dark);text-transform:uppercase}
  .cover-band{position:absolute;left:171px;top:67px;width:157px;height:13px;background:var(--green);
    color:#fff;font-size:5.6px;font-weight:500;line-height:13px;padding-left:6px;white-space:nowrap;text-transform:uppercase}
  .cover-title{position:absolute;right:13px;top:148px;text-align:right;font-family:"Roboto Condensed",Arial,sans-serif;
    font-weight:700;font-size:16px;line-height:19px;color:var(--ink)}
  .cover-rule{position:absolute;left:148px;top:195px;width:180px;height:1px;background:var(--rule)}

  /* Shared headings */
  .panel-title{position:absolute;left:18px;top:36px;font-family:"Roboto Condensed",Arial,sans-serif;font-weight:700;font-size:15.5px;color:var(--green)}
  .panel-rule{position:absolute;left:0;top:61px;height:1px;background:var(--rule)}

  /* What We Do */
  .services{left:111px;top:572px;width:317px;height:478px}
  .services-photo{position:absolute;left:0;top:0;width:100%;height:313px;
    background:linear-gradient(160deg,#f4f1ee 0%,#e9e3de 35%,#d9d4d0 60%,#f5f4f3 100%)}
  .quote-mark{position:absolute;left:12px;top:172px;font-family:Georgia,serif;font-size:64px;color:#555;line-height:1}
  .quote{position:absolute;left:61px;top:219px;width:210px;font-weight:700;font-size:13.3px;line-height:14.6px;color:var(--ink)}
  .services-body{position:absolute;left:0;top:313px;width:100%;height:165px;background:var(--green);color:#fff;
    padding:28px 20px 0 20px;display:grid;grid-template-columns:130px 130px;column-gap:17px;
    font-size:7.3px;line-height:9.2px;text-align:justify}
  .services-body p+p{margin-top:6px}

  /* Property Types */
  .types{left:428px;top:572px;width:208px;height:478px;
    background:linear-gradient(180deg,#fff 0%,#fff 60%,#eceeef 82%,#c9ccd0 100%)}
  .types .panel-rule{width:105px}
  .types-intro{position:absolute;left:18px;top:86px;width:180px;font-size:8.4px;line-height:9.5px;color:var(--ink)}
  .purpose{position:absolute;left:20px;display:flex;align-items:center;gap:9px;width:185px}
  .purpose-icon{width:24px;height:24px;flex:none}
  .purpose-label{font-size:8.5px;font-weight:500;line-height:9.6px;color:var(--green)}
  .types-heading{position:absolute;left:18px;top:364px;font-size:10.6px;font-weight:700;color:#111}
  .types-list{position:absolute;left:22px;top:381px;list-style:none;font-size:10px;font-weight:500;line-height:15.5px;color:#111}
  .types-list li::before{content:"•";margin-right:5px}

  .corridor{left:636px;top:572px;width:113px;height:478px;border-left:5px solid #1d1d1d;border-right:3px solid #1d1d1d;
    background:linear-gradient(180deg,#cfd2d4 0%,#e6e3de 30%,#b79a7e 48%,#e9e8e6 70%,#c8c6c3 100%)}

  /* Get In Touch */
  .contact{left:764px;top:572px;width:317px;height:478px}
  .contact-photo{position:absolute;inset:0;
    background:linear-gradient(180deg,#b8cce0 0%,#d3deea 40%,#c3ced9 70%,#aab6c2 100%)}
  .contact .panel-title{left:19px;top:66px}
  .contact .panel-rule{top:91px;width:131px}
  .turnaround{position:absolute;left:0;top:300px;height:30px;padding:0 14px 0 18px;background:var(--green);color:#fff;
    display:flex;align-items:center;gap:8px;font-size:8.8px;font-weight:700;white-space:nowrap}
  .turnaround svg{width:16px;height:16px;flex:none}
  .contact-box{position:absolute;left:0;top:345px;width:262px;background:var(--grey-box);color:#fff;
    padding:14px 0 12px 18px;font-size:8.6px;font-weight:700;line-height:19px;white-space:nowrap}
</style>
</head>
<body>

  <!-- Front cover -->
  <section class="page cover">
    <div class="cover-photo" role="img" aria-label="Modern apartment tower beside a waterfront promenade under a blue sky"></div>
    <div class="brand">
      <div class="brand-mark"></div>
      <div class="brand-name">Brookmere<br>Valuations</div>
    </div>
    <div class="cover-band">Property Valuation &amp; Advisory Services</div>
    <h1 class="cover-title">Property Valuation &amp;<br>Advisory Services</h1>
    <div class="cover-rule"></div>
  </section>

  <!-- What We Do -->
  <section class="page services">
    <div class="services-photo" role="img" aria-label="Hands typing on a laptop keyboard in a bright office"></div>
    <h2 class="panel-title">What We Do</h2>
    <div class="panel-rule" style="width:100px"></div>
    <div class="quote-mark">&ldquo;</div>
    <p class="quote">Our experts are dedicated to providing high quality valuation advice for every purpose from stamp duty valuations to transactional advice.</p>
    <div class="services-body">
      <div>
        <p>At Brookmere, we provide property valuation and advisory services to individuals, investors, developers and organisations. Our experts are dedicated to providing high quality valuation advice for every purpose from stamp duty valuations to transactional advice.</p>
        <p>Our reliability and proficiency is underpinned by extensive industry</p>
      </div>
      <div>
        <p>experience, highly qualified valuers, independent outlook and direct and transparent advice which allow us to produce reliable market-leading valuation service across a wide range of property types including residential, commercial, retail and industrial.</p>
      </div>
    </div>
  </section>

  <!-- Property Types -->
  <section class="page types">
    <h2 class="panel-title">Property Types</h2>
    <div class="panel-rule"></div>
    <p class="types-intro">We provide valuation advisory for a wide range of purposes.</p>

    <div class="purpose" style="top:113px">
      <svg class="purpose-icon" viewBox="0 0 24 24"><circle cx="12" cy="12" r="12" fill="var(--icon)"/><path d="M6 12.5 12 7l6 5.5h-2V17h-3v-3h-2v3H8v-4.5z" fill="#fff"/></svg>
      <span class="purpose-label">Pre-Purchase and Pre-sale<br>Valuations</span>
    </div>
    <div class="purpose" style="top:146px">
      <svg class="purpose-icon" viewBox="0 0 24 24"><circle cx="12" cy="12" r="12" fill="var(--icon)"/><text x="12" y="16.5" text-anchor="middle" font-family="Roboto, Arial, sans-serif" font-weight="700" font-size="13" fill="#fff">$</text></svg>
      <span class="purpose-label">Stamp Duty Valuations</span>
    </div>
    <div class="purpose" style="top:176px">
      <svg class="purpose-icon" viewBox="0 0 24 24"><circle cx="12" cy="12" r="12" fill="var(--icon)"/><path d="M7 16h2v1H7zM10 14h2v3h-2zM13 11h2v6h-2zM16 8h2v9h-2z" fill="#fff"/></svg>
      <span class="purpose-label">Capital Gains Tax Valuations</span>
    </div>
    <div class="purpose" style="top:204px">
      <svg class="purpose-icon" viewBox="0 0 24 24"><circle cx="12" cy="12" r="12" fill="var(--icon)"/><rect x="9" y="6" width="6" height="12" rx="1" fill="none" stroke="#fff" stroke-width="1.4"/><circle cx="12" cy="16" r=".8" fill="#fff"/></svg>
      <span class="purpose-label">Unit Entitlement Valuations</span>
    </div>
    <div class="purpose" style="top:234px">
      <svg class="purpose-icon" viewBox="0 0 24 24"><circle cx="12" cy="12" r="12" fill="var(--icon)"/><path d="M9 6.5l4 4-1.4 1.4-4-4zM12.5 10l1.5 1.5-5 5-1.5-1.5zM6 17.5h7V19H6z" fill="#fff"/></svg>
      <span class="purpose-label">Family Law &amp; Litigations<br>Valuations</span>
    </div>
    <div class="purpose" style="top:263px">
      <svg class="purpose-icon" viewBox="0 0 24 24"><circle cx="12" cy="12" r="12" fill="var(--icon)"/><circle cx="11" cy="11" r="4" fill="none" stroke="#fff" stroke-width="1.6"/><path d="M14 14l3.5 3.5" stroke="#fff" stroke-width="1.8"/></svg>
      <span class="purpose-label">Easement Valuations</span>
    </div>
    <div class="purpose" style="top:293px">
      <svg class="purpose-icon" viewBox="0 0 24 24"><circle cx="12" cy="12" r="12" fill="var(--icon)"/><path d="M7 17V8M7 17h11" stroke="#fff" stroke-width="1.4" fill="none"/><path d="M9 15h2v-3H9zM12 15h2v-5h-2zM15 15h2V9h-2z" fill="#fff"/></svg>
      <span class="purpose-label">Insolvency / Asset Realisation<br>Valuations</span>
    </div>
    <div class="purpose" style="top:322px">
      <svg class="purpose-icon" viewBox="0 0 24 24"><circle cx="12" cy="12" r="12" fill="var(--icon)"/><path d="M8.5 6h5l2.5 2.5V18h-7.5z" fill="none" stroke="#fff" stroke-width="1.3"/><path d="M10.5 11h3.5M10.5 13.5h3.5M10.5 16h2.5" stroke="#fff" stroke-width="1"/></svg>
      <span class="purpose-label">Wills &amp; Probate Valuations</span>
    </div>

    <p class="types-heading">The 4 main property types are:</p>
    <ul class="types-list">
      <li>Residential</li>
      <li>Commercial</li>
      <li>Industrial</li>
      <li>Retail</li>
    </ul>
  </section>

  <div class="page corridor" role="img" aria-label="Bright shopping centre corridor with polished tiled floor"></div>

  <!-- Get In Touch -->
  <section class="page contact">
    <div class="contact-photo" role="img" aria-label="Dotted map of Australia over silhouettes of business people and a city skyline"></div>
    <h2 class="panel-title">Get In Touch</h2>
    <div class="panel-rule"></div>
    <div class="turnaround">
      <svg viewBox="0 0 16 16"><circle cx="8" cy="8" r="7" fill="none" stroke="#fff" stroke-width="1.5"/><path d="M8 4v4.3l2.8 1.7" fill="none" stroke="#fff" stroke-width="1.5"/></svg>
      Fast 48 hour turnaround on short form valuations
    </div>
    <div class="contact-box">
      Phone: 1300 555 014<br>
      Email: info@brookmerevaluations-example.com.au<br>
      Mail: PO Box 418 Fairhaven NSW 2199<br>
      Web: www.brookmerevaluations-example.com.au
    </div>
  </section>

</body>
</html>
```